Cocktail-Making Assistant App re-design

Ok boys and girls, here's the deal:
I have an android app which is almost complete, but needs a design overhaul.

The app is a standard cocktail-making assistant: gives you a list of cocktails and the ability to see which cocktail you can make out of those ingredients (drinks, fruit, etc) you have at home.

I've attached some general app flow, as well as detailed requirements/explanation presentation. Most of those things are just FYI, so that you know what it's about.

3 screens are the most important (main screen, cocktail view screen, ingredient view screen), meaning I will pick the design mostly based on ideas for those 3 things, with the fourth being a rather simple list (given on attached flow, third tier)
Some other screens are derived from that, with some minor changes on it, but you shouldn't care about that.

There are lots of other, non-explained things which I said nothing about only because they are (from design point of view) completely the same and would only make it seem more complicated.

I don't want to influence the colour scheme, but the app will be released under RedFern developer name (having a light colured red fern as a logo) so I suppose some brownish design, for example, will not really fit nicely. If you, however, have a killer which you are confident will prove me wrong, I'm looking forward to seeing it!

It should be a serious, elegant look (as opposed to cartoonish, but we are not aiming for a business look at all!), not cluttered with details, no clubbing themes, glitter and so on.

Test apk file available on request (Android 2.3+).

Edit: payment is now guaranteed
Also please note that currently, the favorite, "heart" button has a motion effect:
on click it flies out of the screen to the left (white heart) and comes back to the screen as a red heart. Take that into consideration, if it means anything to you.
Updates

Target Market(s)

Whoever you imagine would enjoy drinking cocktails

Industry/Entity Type

Business

Requirements
Must have
• Everything is said in the provided documentation - images say more than I could possibly write here.
Nice to have
• As said, most of the icons are a nice-to-have. Only those which are critically linked to the rest of the design must be provided. More details in the docs.
Should not have
• No cartoon look, No zillion colours

```html
<!DOCTYPE html>
<html lang="en">
<head>
<meta charset="utf-8">
<title>Cocktail Search – App Screens</title>
<link href="https://fonts.googleapis.com/css2?family=Quicksand:wght@400;500&display=swap" rel="stylesheet">
<style>
  :root {
    --page-bg: #d4d5d7;
    --screen-bg: #f1f1f1;
    --screen-glow: #ffffff;
    --ink: #2a2a2a;
    --field-border: #a9a9a9;
    --field-text: #777777;
    --icon-muted: #7a7a7a;
    --label-muted: #6f6f6f;
    --white: #ffffff;

    --soft-header-top: #6fbcdc;
    --soft-header-bottom: #b4dcec;
    --soft-yellow: #faf4aa;
    --soft-teal: #9cddd8;
    --soft-lilac: #e2defa;
    --soft-clay: #e0b8a7;
    --soft-sage: #cddfdc;
    --soft-pink: #f0d0e8;

    --bold-header-top: #1a8ad6;
    --bold-header-mid: #0b78cc;
    --bold-header-bottom: #2aa2e6;
    --yellow-top: #f7e82a; --yellow-bottom: #f6a833;
    --teal-top: #0aa79b; --teal-bottom: #22b374;
    --pink-top: #ef77ab; --pink-bottom: #ec1b74;
    --purple-top: #cf98cc; --purple-bottom: #8a278c;
    --green-top: #8dc63f; --green-bottom: #38b44a;
    --blue-top: #28a8e1; --blue-bottom: #0a6cb7;
  }
  * { box-sizing: border-box; margin: 0; padding: 0; }
  html, body { width: 1200px; height: 868px; overflow: hidden; background: var(--page-bg); }
  body { font-family: "Quicksand", sans-serif; }

  .stage {
    position: relative; width: 1158px; height: 838px;
    transform: scale(1.0363, 1.0358); transform-origin: 0 0;
  }
  .screen {
    position: absolute; top: 36px; width: 433px; height: 764px;
    background: radial-gradient(ellipse 60% 42% at 50% 48%, var(--screen-glow) 0%, var(--screen-bg) 100%);
    overflow: hidden;
  }
  .screen--soft { left: 122px; }
  .screen--bold { left: 577px; }

  .app-bar { position: relative; height: 72px; }
  .screen--soft .app-bar { background: linear-gradient(var(--soft-header-top), var(--soft-header-bottom)); }
  .screen--bold .app-bar { background: linear-gradient(var(--bold-header-top) 0%, var(--bold-header-mid) 55%, var(--bold-header-bottom) 100%); }
  .app-bar__title {
    position: absolute; left: 0; right: 0; top: 18px; text-align: center;
    color: var(--white); font-size: 28px; font-weight: 400; letter-spacing: 0.2px;
  }
  .app-bar__button {
    position: absolute; top: 14px; width: 45px; height: 45px;
    border: 3px solid var(--white); border-radius: 50%;
    display: flex; align-items: center; justify-content: center;
  }
  .app-bar__button--home { left: 13px; }
  .app-bar__button--settings { right: 13px; }

  .search { position: absolute; left: 30px; top: 91px; }
  .search__heading { font-size: 24px; font-weight: 500; color: var(--ink); }
  .search__field {
    position: absolute; left: 18px; top: 43px; width: 345px; height: 39px;
    border: 3px solid var(--field-border); background: var(--white);
    font-size: 14px; color: var(--field-text); padding: 6px 0 0 12px;
  }
  .search__icon { position: absolute; right: 12px; top: 6px; }

  .category-grid {
    position: absolute; left: 9px; top: 249px;
    display: grid; grid-template-columns: 203px 203px; grid-auto-rows: 125px; gap: 7px;
  }
  .category {
    position: relative; display: flex; flex-direction: column; align-items: center;
  }
  .category__icon { margin-top: 14px; width: 72px; height: 72px; }
  .category__label { position: absolute; bottom: 7px; font-size: 16px; font-weight: 500; }

  .screen--soft .category__icon { color: var(--icon-muted); }
  .screen--soft .category__label { color: var(--label-muted); }
  .screen--bold .category__icon { color: var(--white); }
  .screen--bold .category__label { color: var(--white); font-size: 19px; }

  .soft-yellow { background: var(--soft-yellow); }
  .soft-teal { background: var(--soft-teal); }
  .soft-lilac { background: var(--soft-lilac); }
  .soft-clay { background: var(--soft-clay); }
  .soft-sage { background: var(--soft-sage); }
  .soft-pink { background: var(--soft-pink); }

  .bold-yellow { background: linear-gradient(var(--yellow-top), var(--yellow-bottom)); }
  .bold-teal { background: linear-gradient(var(--teal-top), var(--teal-bottom)); }
  .bold-pink { background: linear-gradient(var(--pink-top), var(--pink-bottom)); }
  .bold-purple { background: linear-gradient(var(--purple-top), var(--purple-bottom)); }
  .bold-green { background: linear-gradient(var(--green-top), var(--green-bottom)); }
  .bold-blue { background: linear-gradient(var(--blue-top), var(--blue-bottom)); }
</style>
</head>
<body>
<svg width="0" height="0" style="position:absolute" aria-hidden="true">
  <defs>
    <symbol id="icon-home" viewBox="0 0 24 24">
      <path d="M12 3 L2 12 H5 V21 H10 V15 H14 V21 H19 V12 H22 Z" fill="#ffffff"/>
    </symbol>
    <symbol id="icon-gear" viewBox="0 0 24 24">
      <g fill="#ffffff">
        <circle cx="12" cy="12" r="7.5"/>
        <g>
          <rect x="10.2" y="1.5" width="3.6" height="21" rx="1"/>
          <rect x="10.2" y="1.5" width="3.6" height="21" rx="1" transform="rotate(45 12 12)"/>
          <rect x="10.2" y="1.5" width="3.6" height="21" rx="1" transform="rotate(90 12 12)"/>
          <rect x="10.2" y="1.5" width="3.6" height="21" rx="1" transform="rotate(135 12 12)"/>
        </g>
      </g>
      <circle cx="12" cy="12" r="3.2" fill="currentColor"/>
    </symbol>
    <symbol id="icon-wine" viewBox="0 0 72 72">
      <g fill="none" stroke="currentColor" stroke-width="4" stroke-linecap="round" stroke-linejoin="round">
        <path d="M24 8 H48 C52 20 50 36 36 40 C22 36 20 20 24 8 Z"/>
        <path d="M24 17 C30 13 42 21 49 16"/>
        <path d="M36 40 V64 M25 64 H47"/>
      </g>
    </symbol>
    <symbol id="icon-martini" viewBox="0 0 72 72">
      <g fill="none" stroke="currentColor" stroke-width="4" stroke-linecap="round" stroke-linejoin="round">
        <path d="M12 30 H56 L34 52 Z"/>
        <path d="M34 52 V66 M23 66 H45"/>
        <path d="M28 46 L50 6 L58 4"/>
        <path d="M54 2 L58 4 L56 9"/>
      </g>
    </symbol>
    <symbol id="icon-juice" viewBox="0 0 72 72">
      <g fill="none" stroke="currentColor" stroke-width="4" stroke-linecap="round" stroke-linejoin="round">
        <path d="M16 24 H56 L50 66 H22 Z"/>
        <path d="M24 40 H48 L46 56 H26 Z"/>
        <path d="M18 6 L30 12 L36 48"/>
      </g>
    </symbol>
    <symbol id="icon-cup" viewBox="0 0 72 72">
      <g fill="none" stroke="currentColor" stroke-width="4" stroke-linecap="round" stroke-linejoin="round">
        <path d="M17 16 H55 V24 H17 Z"/>
        <path d="M22 10 H50 V16 H22 Z"/>
        <path d="M20 24 L25 66 H47 L52 24"/>
      </g>
    </symbol>
    <symbol id="icon-bubbles" viewBox="0 0 72 72">
      <g fill="none" stroke="currentColor" stroke-width="4">
        <circle cx="22" cy="20" r="11"/>
        <circle cx="46" cy="14" r="8"/>
        <circle cx="40" cy="46" r="17"/>
      </g>
    </symbol>
    <symbol id="icon-burst" viewBox="0 0 72 72">
      <path d="M36 10 L42 24 L58 18 L51 32 L64 40 L49 44 L52 60 L39 50 L28 62 L27 46 L10 44 L22 34 L14 20 L30 24 Z"
            fill="none" stroke="currentColor" stroke-width="3.5" stroke-linejoin="round"/>
    </symbol>
    <symbol id="icon-magnifier" viewBox="0 0 24 24">
      <g fill="none" stroke="#e2e2e2" stroke-width="3" stroke-linecap="round">
        <circle cx="9" cy="9" r="6"/>
        <path d="M14 14 L21 20"/>
      </g>
    </symbol>
  </defs>
</svg>

<main class="stage">
  <section class="screen screen--soft" aria-label="Cocktail Search, pastel theme">
    <header class="app-bar">
      <span class="app-bar__button app-bar__button--home"><svg width="22" height="22"><use href="#icon-home"/></svg></span>
      <h1 class="app-bar__title">Cocktail Search</h1>
      <span class="app-bar__button app-bar__button--settings" style="color:#94cfe4"><svg width="27" height="27"><use href="#icon-gear"/></svg></span>
    </header>
    <div class="search">
      <h2 class="search__heading">Search</h2>
      <div class="search__field">Tap here to edit text &nbsp;. . .
        <svg class="search__icon" width="24" height="24"><use href="#icon-magnifier"/></svg>
      </div>
    </div>
    <nav class="category-grid">
      <a class="category soft-yellow"><svg class="category__icon"><use href="#icon-wine"/></svg><span class="category__label">Liquor / Cordial</span></a>
      <a class="category soft-teal"><svg class="category__icon"><use href="#icon-martini"/></svg><span class="category__label">Syrup / Mixer</span></a>
      <a class="category soft-lilac"><svg class="category__icon"><use href="#icon-juice"/></svg><span class="category__label">Fruit / Juice</span></a>
      <a class="category soft-clay"><svg class="category__icon"><use href="#icon-cup"/></svg><span class="category__label">Garnish / Spice</span></a>
      <a class="category soft-sage"><svg class="category__icon"><use href="#icon-bubbles"/></svg><span class="category__label">Other Spirit</span></a>
      <a class="category soft-pink"><svg class="category__icon"><use href="#icon-burst"/></svg><span class="category__label">All</span></a>
    </nav>
  </section>

  <section class="screen screen--bold" aria-label="Cocktail Search, vivid theme">
    <header class="app-bar">
      <span class="app-bar__button app-bar__button--home"><svg width="22" height="22"><use href="#icon-home"/></svg></span>
      <h1 class="app-bar__title">Cocktail Search</h1>
      <span class="app-bar__button app-bar__button--settings" style="color:#0f7fcf"><svg width="27" height="27"><use href="#icon-gear"/></svg></span>
    </header>
    <div class="search">
      <h2 class="search__heading">Search</h2>
      <div class="search__field">Tap here to edit text &nbsp;. . .
        <svg class="search__icon" width="24" height="24"><use href="#icon-magnifier"/></svg>
      </div>
    </div>
    <nav class="category-grid">
      <a class="category bold-yellow"><svg class="category__icon"><use href="#icon-wine"/></svg><span class="category__label">Liquor / Cordial</span></a>
      <a class="category bold-teal"><svg class="category__icon"><use href="#icon-martini"/></svg><span class="category__label">Syrup / Mixer</span></a>
      <a class="category bold-pink"><svg class="category__icon"><use href="#icon-juice"/></svg><span class="category__label">Fruit / Juice</span></a>
      <a class="category bold-purple"><svg class="category__icon"><use href="#icon-cup"/></svg><span class="category__label">Garnish / Spice</span></a>
      <a class="category bold-green"><svg class="category__icon"><use href="#icon-bubbles"/></svg><span class="category__label">Other Spirit</span></a>
      <a class="category bold-blue"><svg class="category__icon"><use href="#icon-burst"/></svg><span class="category__label">All</span></a>
    </nav>
  </section>
</main>
</body>
</html>
```